Baseball Coaching Camp for 5-14year olds needs sales campaign

Local baseball coaching camp for children is in it's 22nd year running a 4-5 week series of summer camps. Each year we use email marketing beginning around December to sell our camps to the parents to sign up their children for one or more weeks. All information about the camps can be seen on our website at https://quernhill.net/. In the past we have had success by changing the look of the emails each month and offering a decreasing discount as the camps get closer.

Our target market is the parents of children ages 5-14years old who like and play baseball and are interested in improving their skills in a fun environment during the Summer months.

We would like to improve the sales by developing new creative and imaginative emails for this season. We need 6 to 8 quality ads that can somehow relate to each other , these ads will be sent via our mailing list as well as used on social media. One of the owners thought it would be nice to use the "lantern harbor" theme though we are open to all ideas.
We have given you access to a dropbox link with examples of past campaigns along with artwork and images here
https://www.filecrate.example/sh/q7tmwpz2kdrlvha/BBKfe-moWenaXr7QuLP815cXo?dl=0

```html
<!DOCTYPE html>
<html lang="en">
<head>
<meta charset="utf-8">
<title>Lantern Harbor – Quernhill Baseball Camp</title>
<link href="https://fonts.googleapis.com/css2?family=Oswald:wght@400;500;600;700&family=Playfair+Display:wght@900&family=Poppins:wght@400;500;600;700&family=Raleway:wght@400&display=swap" rel="stylesheet">
<style>
  :root{
    --page:#e0e1e3;
    --card:#f5f5f5;
    --grass-dark:#2f6a1e;
    --grass-light:#5da536;
    --ink:#1c1712;
    --yellow:#ffd200;
    --orange:#f7901e;
    --red:#f5122b;
    --navy:#001f6e;
    --white:#ffffff;
    --schedule-text:#5a4300;
  }
  *{box-sizing:border-box;margin:0;padding:0}
  html,body{width:1200px;height:2306px;overflow:hidden;background:var(--page)}
  body{position:relative;font-family:'Poppins',sans-serif}
  .email-card{position:absolute;left:210px;top:0;width:780px;height:2240px;background:var(--card)}
  .email{position:absolute;left:30px;top:31px;width:720px}
  section{position:relative;width:720px;overflow:hidden}

  .masthead{height:202px;background:radial-gradient(ellipse at 50% 20%,var(--grass-light),var(--grass-dark) 80%)}
  .brand{position:absolute;left:40px;top:78px;display:flex;align-items:center;gap:12px}
  .brand-dot{width:44px;height:44px;border-radius:50%;background:var(--ink)}
  .brand-name{font-family:'Oswald',sans-serif;font-weight:600;font-size:34px;color:var(--ink);letter-spacing:1px}
  .masthead-title{position:absolute;right:26px;top:40px;text-align:right;color:var(--white);font-family:'Oswald',sans-serif;font-weight:700;line-height:1}
  .masthead-title .small{font-size:38px;letter-spacing:1px}
  .masthead-title .big{font-size:80px;letter-spacing:3px;margin-top:4px}

  .hero{height:701px;background:linear-gradient(160deg,#1e2226 0%,#2c3136 45%,#3a4038 70%,#2e6b22 100%)}
  .hero-photo{position:absolute;right:0;top:260px;width:460px;height:441px;background:radial-gradient(ellipse at 60% 45%,#f2b21c 0%,#c98d1a 40%,rgba(60,120,30,.9) 75%,#2f6a1e 100%)}
  .hero-kicker{position:absolute;left:26px;top:50px;font-family:'Oswald',sans-serif;font-weight:500;font-size:64px;color:#fff56a;line-height:1}
  .hero-title{position:absolute;left:24px;top:116px;font-family:'Playfair Display',serif;font-weight:900;font-size:96px;color:var(--orange);line-height:1;letter-spacing:2px}
  .hero-sub{position:absolute;left:26px;top:226px;font-family:'Raleway',sans-serif;font-size:33px;color:var(--white)}
  .hero-year{position:absolute;left:20px;top:278px;font-family:'Poppins',sans-serif;font-weight:700;font-size:164px;color:var(--yellow);line-height:1;letter-spacing:-4px}
  .register-tag{position:absolute;left:24px;top:438px;width:346px;height:52px;background:var(--red);border-radius:10px 0 0 10px;font-family:'Oswald',sans-serif;font-style:italic;font-weight:500;font-size:28px;color:var(--white);line-height:52px;padding-left:20px;letter-spacing:1px}
  .price-splash{position:absolute;left:0;top:500px;width:330px;height:201px}
  .price-text{position:absolute;left:26px;top:540px;transform:rotate(-5deg);transform-origin:left top;color:var(--white)}
  .price-text .label{font-family:'Oswald',sans-serif;font-weight:600;font-size:22px;letter-spacing:1px}
  .price-text .amount{font-family:'Poppins',sans-serif;font-weight:700;font-size:60px;line-height:1.1}

  .skills{height:525px;background:linear-gradient(180deg,#5a5248 0%,#8a7a62 35%,#c9a47c 60%,#dcb48a 85%,#6f9a40 100%)}
  .skill-list{list-style:none;position:absolute;left:0;top:119px}
  .skill-list li{width:144px;height:48px;background:var(--yellow);border-radius:0 24px 24px 0;border-right:5px solid var(--ink);font-weight:600;font-size:22px;color:var(--ink);line-height:48px;padding-left:14px;margin-bottom:16px}

  .signup-bar{height:131px;background:var(--ink);color:var(--white)}
  .ages{position:absolute;left:31px;top:32px}
  .ages .label{font-size:19px;font-weight:500}
  .ages .range{font-size:46px;font-weight:700;line-height:1.1}
  .signup-copy{position:absolute;left:209px;top:40px;font-weight:600;font-size:25px;line-height:31px;letter-spacing:1.5px}
  .signup-button{position:absolute;left:476px;top:41px;width:216px;height:60px;background:var(--red);color:var(--white);font-weight:700;font-size:36px;line-height:62px;text-align:center;letter-spacing:1px}

  .schedule{height:301px;background:var(--yellow);padding:26px 2px 0 20px}
  .schedule-heading{display:flex;align-items:center;gap:8px;font-weight:700;font-size:30px;color:var(--ink)}
  .schedule-heading::after{content:"";flex:1;height:3px;background:var(--ink);margin-top:12px}
  .schedule-list{list-style:none;margin-top:18px}
  .schedule-list li{font-size:22px;color:var(--schedule-text);height:44px;letter-spacing:.5px}
  .schedule-list b{font-weight:700}

  .contact{height:208px;background:var(--navy);text-align:center}
  .contact-note{padding-top:26px;font-weight:500;font-size:29px;color:var(--white);letter-spacing:1px}
  .contact-phone{font-family:'Oswald',sans-serif;font-weight:600;font-size:76px;color:var(--yellow);line-height:1.2;letter-spacing:2px}

  .social{position:absolute;left:354px;top:2132px;display:flex;gap:12px}
  .social span{width:60px;height:60px;border-radius:50%}
  .social .one{background:#0d3fb8}
  .social .two{background:#c7389f}
</style>
</head>
<body>
<div class="email-card">
  <div class="email">
    <section class="masthead">
      <div class="brand"><span class="brand-dot"></span><span class="brand-name">QUERNHILL</span></div>
      <div class="masthead-title"><div class="small">QUERNHILL BASEBALL</div><div class="big">ACADEMY</div></div>
    </section>

    <section class="hero">
      <div class="hero-photo" role="img" aria-label="Young player in a yellow camp shirt and batting helmet sliding head-first onto the grass"></div>
      <div class="hero-kicker">LANTERN</div>
      <div class="hero-title">HARBOR</div>
      <div class="hero-sub">QUERNHILL BASEBALL CAMP</div>
      <div class="hero-year">2021</div>
      <div class="register-tag">OPEN FOR REGISTRATION</div>
      <svg class="price-splash" viewBox="0 0 330 201" aria-hidden="true">
        <polygon points="0,40 60,28 140,18 220,8 300,0 318,24 300,70 270,120 240,160 215,201 0,201" fill="#111"/>
      </svg>
      <div class="price-text"><div class="label">PRICING STARTS AT</div><div class="amount">$225</div></div>
    </section>

    <section class="skills" role="img" aria-label="Campers in yellow shirts running the bases on a dirt infield">
      <ul class="skill-list">
        <li>Hitting</li><li>Pitching</li><li>Catching</li><li>Fielding</li>
      </ul>
    </section>

    <section class="signup-bar">
      <div class="ages"><div class="label">Youth Ages</div><div class="range">5 – 14</div></div>
      <div class="signup-copy">SIGN UP TODAY<br>&amp; SAVE MONEY</div>
      <div class="signup-button">SIGN UP</div>
    </section>

    <section class="schedule">
      <h2 class="schedule-heading">CHOOSE SCHEDULE</h2>
      <ul class="schedule-list">
        <li><b>Week 1:</b> Dec 01 - Dec 05 at Town Park, Alderwick</li>
        <li><b>Week 2:</b> Dec 01 - Dec 05 at Fireman’s Field, Brookmere</li>
        <li><b>Week 3:</b> Dec 01 - Dec 05 at Hollis Park, Fenbridge</li>
        <li><b>Week 4:</b> Dec 01 - Dec 05 at Town Park, Alderwick</li>
      </ul>
    </section>

    <section class="contact">
      <p class="contact-note">For more queries please call us.</p>
      <p class="contact-phone">(555) 014-2290</p>
    </section>
  </div>
</div>
<div class="social" aria-label="Social links"><span class="one"></span><span class="two"></span></div>
</body>
</html>
```